Velmora Company needs a Business Card Design

We just opened our business recently and we need a business card design. Our basic product are clothes and accessories. We would like to see designs that use bright colors like pink, light blue and purple. In addition to that kindly include also our address in the business card which our main office is located in Los Angeles, California.
The final design should communicate that we have affordable price yet high quality brand.

Target Market(s)

young and middle age women

Industry/Entity Type

Business

Contact Information for Business Card

Velmora Apparel and Accessories 3847 North Hollis St. Los Angeles California
Tel: 424-583-6094

Logo Text

Velmora's Apparel and Accessories

Font styles to use
Serif

Requirements
Must have
• there should be a graphic of a sexy lady wearing an elegant dress at the upper left corner of the business card.

```html
<!DOCTYPE html>
<html lang="en">
<head>
<meta charset="UTF-8">
<title>Velmora Apparel and Accessories – Business Card</title>
<link rel="stylesheet" href="https://fonts.googleapis.com/css2?family=Arimo:wght@400;700&display=swap">
<style>
  :root {
    --page-bg: #eef1f7;
    --card-top: #b4c0e0;
    --card-bottom: #9fb0d8;
    --brand-magenta: #b4288f;
    --ink: #2b2b33;
    --figure-dark: #111114;
  }
  * { margin: 0; padding: 0; box-sizing: border-box; }
  html, body {
    width: 1200px;
    height: 902px;
    overflow: hidden;
    background: var(--page-bg);
    font-family: "Arimo", Arial, sans-serif;
  }
  .canvas {
    position: relative;
    width: 1200px;
    height: 902px;
  }
  .business-card {
    position: absolute;
    left: 100px;
    top: 166px;
    width: 1000px;
    height: 570px;
    border-radius: 22px;
    background: linear-gradient(160deg, var(--card-top), var(--card-bottom));
    box-shadow: 0 10px 30px rgba(40, 60, 110, 0.18);
    overflow: hidden;
  }
  .lady-illustration {
    position: absolute;
    left: 96px;
    top: 47px;
    width: 175px;
    height: 494px;
    border-radius: 88px 88px 20px 20px;
    background: linear-gradient(180deg, var(--figure-dark) 0%, #2a1a28 45%, var(--figure-dark) 100%);
    opacity: 0.9;
  }
  .brand-block {
    position: absolute;
    right: 119px;
    top: 66px;
    text-align: right;
  }
  .brand-name {
    font-size: 84px;
    font-weight: 400;
    line-height: 1;
    color: var(--brand-magenta);
  }
  .brand-tagline {
    margin-top: 26px;
    font-size: 31px;
    font-weight: 400;
    line-height: 1;
    color: var(--ink);
  }
  .contact-block {
    position: absolute;
    left: 628px;
    top: 378px;
    transform: translateX(-50%);
    text-align: center;
    white-space: nowrap;
    font-style: normal;
    color: var(--ink);
  }
  .contact-phone {
    font-size: 47px;
    line-height: 1;
  }
  .contact-address {
    margin-top: 22px;
    font-size: 24px;
    line-height: 1;
  }
</style>
</head>
<body>
  <main class="canvas">
    <section class="business-card">
      <div class="lady-illustration" role="img" aria-label="Silhouette illustration of an elegant woman in a long black gown with pink gloves and earrings"></div>

      <header class="brand-block">
        <h1 class="brand-name">Velmora</h1>
        <p class="brand-tagline">Apparel and Accessories</p>
      </header>

      <address class="contact-block">
        <p class="contact-phone">Tel: 424-583-6094</p>
        <p class="contact-address">3847 North Hollis St. Los Angeles California</p>
      </address>
    </section>
  </main>
</body>
</html>
```